Poster for an advertising campaign

Hi, we are an agency, our business is to orienteates student to study abroad in Germany. For that, we enroll them in language schools in Germany and help them to find an accomodation.
We are going to launch an advertising campaign through Rural advertising signs.
- Need to have our Movarel Center logo
- Need to have these 2 mentions :
1/ Etudes en Allemagne et accompagnement durant toute la procédure.
2/ Cours de langue allemande
- If possible put as a signature ; in small characters our brand essence ( Excellence Through Education ) Maybe at the bottom right of the logo
For the format it will be 3.5m*2.5m , more format adaptations will be shared as soon as we finalize the crea
- We would like to have the logo in 2D ,like for the attached simulation
- Need to have interesting backgrounds and designs in line with our identity & service ( studying in Germany , learn the German language , the support &the accompaniment during all the procedure …) ,knowing as well that our target is bachelors , bac students …
Thx

```html
<!DOCTYPE html>
<html lang="fr">
<head>
<meta charset="utf-8">
<title>Movarel Center – Etudes en Allemagne</title>
<link rel="stylesheet" href="https://fonts.googleapis.com/css2?family=Bebas+Neue&family=Open+Sans:wght@400&display=swap">
<style>
  :root {
    --navy-top: #0d1c4e;
    --navy-mid: #0a1538;
    --navy-deep: #060b1e;
    --ink-white: #ffffff;
    --accent-yellow: #e2dd1f;
    --frame-grey: #7a7d86;
  }
  html, body {
    margin: 0;
    padding: 0;
    width: 1200px;
    height: 1200px;
    overflow: hidden;
    background: var(--navy-deep);
  }
  .poster {
    position: relative;
    width: 1200px;
    height: 1200px;
    overflow: hidden;
    background: linear-gradient(170deg, var(--navy-top) 0%, var(--navy-mid) 40%, var(--navy-deep) 100%);
    font-family: "Bebas Neue", "Oswald", sans-serif;
  }
  .backdrop-photo {
    position: absolute;
    inset: 0;
    background: radial-gradient(ellipse at 55% 60%, rgba(40, 55, 95, 0.35) 0%, rgba(10, 20, 50, 0) 60%);
  }
  .frame {
    position: absolute;
    inset: 12px;
    border: 2px solid var(--frame-grey);
    pointer-events: none;
  }
  .brand {
    position: absolute;
    left: 66px;
    top: 120px;
    display: flex;
    align-items: center;
    gap: 18px;
    color: var(--ink-white);
    line-height: 0.85;
  }
  .brand-dot {
    width: 34px;
    height: 34px;
    border-radius: 50%;
    background: var(--accent-yellow);
    flex: none;
  }
  .brand-name {
    display: flex;
    flex-direction: column;
  }
  .brand-name .word-main { font-size: 104px; }
  .brand-name .word-sub { font-size: 62px; letter-spacing: 2px; text-align: right; }

  .headline {
    position: absolute;
    left: 480px;
    top: 40px;
    width: 680px;
    color: var(--ink-white);
    margin: 0;
    font-weight: 400;
    line-height: 1;
  }
  .headline .line-main {
    display: block;
    font-size: 242px;
    letter-spacing: 20px;
    line-height: 0.92;
  }
  .headline .line-sub {
    display: block;
    font-size: 112px;
    letter-spacing: 8px;
    word-spacing: 18px;
    margin-top: 4px;
  }
  .service {
    position: absolute;
    left: 0;
    right: 0;
    top: 505px;
    text-align: center;
    color: var(--accent-yellow);
  }
  .service-support {
    margin: 0;
    font-family: "Open Sans", "Segoe UI", sans-serif;
    font-size: 39px;
    line-height: 52px;
    font-weight: 400;
    text-transform: uppercase;
  }
  .service-course {
    margin: 10px 0 0;
    font-size: 78px;
    letter-spacing: 2px;
    line-height: 1;
  }
  .tagline {
    position: absolute;
    left: 38px;
    top: 878px;
    margin: 0;
    color: var(--ink-white);
    font-size: 98px;
    line-height: 100px;
    letter-spacing: 1px;
  }
  .signature-lettering {
    position: absolute;
    right: 20px;
    bottom: 20px;
    width: 300px;
    height: 240px;
    background: radial-gradient(ellipse at 60% 55%, rgba(226, 221, 31, 0.18) 0%, rgba(226, 221, 31, 0) 70%);
  }
</style>
</head>
<body>
  <main class="poster">
    <div class="backdrop-photo" role="img" aria-label="Faint photo of graduation caps tossed in the air over a dark blue sky"></div>
    <div class="frame"></div>

    <div class="brand">
      <span class="brand-dot"></span>
      <span class="brand-name">
        <span class="word-main">Movarel</span>
        <span class="word-sub">Center</span>
      </span>
    </div>

    <h1 class="headline">
      <span class="line-main">Etudes</span>
      <span class="line-sub">En Allemagne</span>
    </h1>

    <section class="service">
      <p class="service-support">Etudes en Allemagne et accompagnement<br>durant toute la procédure</p>
      <p class="service-course">“Cours de langue allemande”</p>
    </section>

    <p class="tagline">Excellence<br>Through<br>Education</p>

    <div class="signature-lettering" role="img" aria-label="Hand-lettered word Germany with yellow arcs"></div>
  </main>
</body>
</html>
```